Curves, Cups and Commerce needs a book cover

I've been in lingerie business for 12 years, we own 5 x Lingerie stores. This is my story aimed at women in business or women who want to start a business. Essentially its a business book but also offers bra fitting advice. Although the book cover can be a bit cheeky it also needs to be tasteful. I do not have a colour in mind I just don't like it too girly. I like strong and bold with a feminine touch. The title needs to catch peoples attention when surrounded by so many other books. It needs to have some sort of image or texture. That could be a lace background texture. I like the idea of a bra hanging off the letters or some kind of image of a bra but a beautiful lacy bra. I would like the cover to be more beautiful than tacky even though it has the word 'boobs'.
Updates

Hi everyone, some great designs so far. Many of you have made a bra part of the 'Boobs' word. I thought this could work but it doesn't as it covers up the word 'Boobs' too much and I feel this word will catch peoples attention. If any of you would like to revise please feel free. thankyou Delia.

Target Market(s)

Women in business or women wanting to start a business.

Industry/Entity Type

Retail

Logo Text

Curves, Cups and Commerce

Font styles to use
Serif
Sans Serif

Colors

Designer to choose colors to be used in the design.

Requirements
Must have
• Title: Curves, Cups and Commerce (you could replace 'and' with '&' if it works better.
• Tagline: Elevating Lessons for Female Founders
• Author: Delia Forsgate
Nice to have
• An image of a bra, maybe in a playful way. It could hang off the letters or maybe the letters could look like a bra, but I'm concerned it may look tacky that way. Somehow incorporate a picture of a bra preferably as part of the title.
• I don't have images for you, you have the freedom to choose.
Should not have
• Although this book has boobs and bras in the title it must not be tacky or sexual. It is a business book.
• I do not like it to look too girly, probably not script unless its subtle.

```html
<!DOCTYPE html>
<html lang="en">
<head>
<meta charset="utf-8">
<title>Curves, Cups and Commerce – Book Cover</title>
<link rel="stylesheet" href="https://fonts.googleapis.com/css2?family=Montserrat:wght@300;400;900&display=swap">
<style>
  :root {
    --backdrop: #e6e5e1;
    --cover-bg: #fbeaf0;
    --lace-pink: #f6aedb;
    --lace-light: #fbd3ea;
    --charcoal: #4a4a4a;
    --charcoal-deep: #2c2c2c;
    --title-pink: #ef7fc6;
    --title-pink-deep: #cf4a9e;
    --white: #ffffff;
  }
  html, body {
    margin: 0;
    padding: 0;
    width: 1200px;
    height: 1200px;
    overflow: hidden;
    background: var(--backdrop);
  }
  .cover {
    position: absolute;
    left: 180px;
    top: 0;
    width: 840px;
    height: 1200px;
    background: var(--cover-bg);
    overflow: hidden;
    font-family: "Montserrat", sans-serif;
  }
  .lace-band {
    position: absolute;
    left: 0;
    width: 840px;
    height: 180px;
    background: linear-gradient(180deg, var(--lace-pink), var(--lace-light));
  }
  .lace-band--top { top: 0; }
  .lace-band--bottom {
    bottom: 0;
    height: 155px;
    background: linear-gradient(0deg, var(--lace-pink), var(--lace-light));
  }
  .bra-photo {
    position: absolute;
    left: 72px;
    top: 372px;
    width: 168px;
    height: 268px;
    border-radius: 60px;
    background: radial-gradient(circle at 55% 30%, #f39bd2, #d3559f 70%);
  }
  .title {
    position: absolute;
    left: 0;
    top: 0;
    width: 840px;
    height: 720px;
  }
  .title text {
    font-family: "Montserrat", sans-serif;
    font-weight: 900;
  }
  .title .word-dark { fill: var(--charcoal); }
  .title .word-dark-depth { fill: var(--charcoal-deep); }
  .title .word-pink { fill: var(--title-pink); }
  .title .word-pink-depth { fill: var(--title-pink-deep); }
  .tagline {
    position: absolute;
    left: 103px;
    top: 746px;
    width: 650px;
    height: 133px;
    border: 2px solid var(--charcoal-deep);
    display: flex;
    align-items: center;
    justify-content: center;
    text-align: center;
    font-weight: 300;
    font-size: 41px;
    line-height: 1.3;
    letter-spacing: 1px;
    color: #333333;
    text-transform: uppercase;
    margin: 0;
  }
  .author-band {
    position: absolute;
    left: 0;
    top: 953px;
    width: 840px;
    height: 64px;
    background: var(--charcoal);
    color: var(--white);
    display: flex;
    align-items: center;
    justify-content: center;
    font-weight: 400;
    font-size: 38px;
    letter-spacing: 1.5px;
    text-transform: uppercase;
    margin: 0;
  }
</style>
</head>
<body>
  <main class="cover">
    <div class="lace-band lace-band--top" role="img" aria-label="Pink scalloped lace trim border"></div>

    <svg class="title" viewBox="0 0 840 720" role="heading" aria-level="1" aria-label="Curves, Cups and Commerce">
      <text class="word-dark-depth" x="116" y="426" font-size="170" textLength="655" lengthAdjust="spacingAndGlyphs">CURVES</text>
      <text class="word-dark" x="110" y="420" font-size="170" textLength="655" lengthAdjust="spacingAndGlyphs">CURVES</text>

      <text class="word-pink-depth" x="261" y="601" font-size="200" textLength="505" lengthAdjust="spacingAndGlyphs">UPS</text>
      <text class="word-pink" x="255" y="595" font-size="200" textLength="505" lengthAdjust="spacingAndGlyphs">UPS</text>

      <text class="word-dark-depth" x="113" y="688" font-size="50" textLength="130" lengthAdjust="spacingAndGlyphs">AND</text>
      <text class="word-dark" x="110" y="685" font-size="50" textLength="130" lengthAdjust="spacingAndGlyphs">AND</text>
      <text class="word-dark-depth" x="265" y="694" font-size="88" textLength="495" lengthAdjust="spacingAndGlyphs">COMMERCE</text>
      <text class="word-dark" x="260" y="689" font-size="88" textLength="495" lengthAdjust="spacingAndGlyphs">COMMERCE</text>
    </svg>

    <div class="bra-photo" role="img" aria-label="Photo of a pink lace bra hanging vertically, forming the letter C"></div>

    <p class="tagline">Elevating Lessons for<br>Female Founders</p>

    <p class="author-band">Author: Delia Forsgate</p>

    <div class="lace-band lace-band--bottom" role="img" aria-label="Pink scalloped lace trim border"></div>
  </main>
</body>
</html>
```